Business Card Design Project

We need a business card design for our company kV7 s.r.o. The company is based in Slovakia and selling massage, yoga and meditation accessories online and offline. At the place where the offices are, we have a yoga studio, massage room, show room and shop as well. We will give the business card for customers who visit our shop or show room personally and for the new suppliers of demanded products we are visiting in the future.
I would like to have:
- small logo and datas on one side
- big logo and our main e-shops on the other side:
- www.pohodanoviny.sk
- www.relaxbrodeky.cz
Datas:
Peter Hulka, MSc. / CEO
kV7 s.r.o.
Brezovanská 742/3
931 05 Nová Breza
Slovak republic (Slovakia)
Office tel.: +421 (0) 947 618 204
Private tel.: +421 (0) 907 251 836
E-mail: info@kv7example.sk
Web: www.kv7example.sk
It is up to you if you use graphics emphasizing our profile or leave it simple and modern without pics. Looking forward to receiving your designs! Thank You!
Industry/Entity Type
Massage
Colors
Designer to choose colors to be used in the design.
Look and feel
Each slider illustrates characteristics of the customer's brand and the style your logo design should communicate.

```html
<!DOCTYPE html>
<html lang="sk">
<head>
<meta charset="utf-8">
<title>KV7 s.r.o. – business card</title>
<link rel="stylesheet" href="https://fonts.googleapis.com/css2?family=Quicksand:wght@500;600;700&display=swap">
<style>
  :root {
    --orange: #f28021;
    --card-black: #1f1f20;
    --card-dark: #262627;
    --stage: #303132;
    --white: #ffffff;
    --url-grey: #8d8f92;
    --rule: #6a6a6b;
  }
  * { margin: 0; padding: 0; box-sizing: border-box; }
  html, body {
    width: 1200px; height: 926px; overflow: hidden;
    background: var(--stage);
    font-family: "Quicksand", sans-serif;
  }
  .card {
    position: absolute; left: 290px;
    width: 620px; height: 354px;
    border-radius: 16px; overflow: hidden;
    background: var(--card-black);
    box-shadow: 0 10px 30px rgba(0,0,0,.45);
  }
  .card--front { top: 70px; }
  .card--back { top: 500px; background: var(--card-dark); }
  .card__shapes { position: absolute; inset: 0; }

  /* front */
  .front-mark {
    position: absolute; left: 0; right: 0; top: 150px;
    text-align: center;
    font-size: 72px; font-weight: 700; letter-spacing: .08em;
    color: var(--white); line-height: 1;
  }
  .front-shops {
    position: absolute; left: 0; right: 0; top: 282px;
    text-align: center; font-size: 15px; font-weight: 600;
    letter-spacing: .06em; color: var(--url-grey);
  }

  /* back */
  .contact { position: absolute; left: 40px; top: 62px; width: 308px; color: var(--white); font-size: 15px; }
  .contact__row { display: flex; align-items: flex-start; padding: 8px 0; border-bottom: 1px solid var(--rule); }
  .contact__row:last-child { border-bottom: none; }
  .contact__icon { width: 24px; flex: none; margin-left: 8px; margin-top: 2px; }
  .contact__lines { display: grid; grid-template-columns: 64px auto; row-gap: 2px; margin-left: 10px; }
  .contact__label { font-weight: 700; }
  .contact__value { font-weight: 500; }
  .contact__address { margin-left: 10px; line-height: 1.5; font-weight: 500; }

  .owner { position: absolute; left: 370px; top: 72px; width: 250px; color: var(--white); text-align: center; }
  .owner__name { font-size: 19px; font-weight: 700; }
  .owner__title { font-size: 13px; font-weight: 500; }
  .owner__company { font-size: 12px; font-weight: 700; margin-top: 2px; }
  .back-mark {
    position: absolute; left: 400px; top: 226px; width: 200px;
    text-align: center;
    font-size: 50px; font-weight: 700; letter-spacing: .08em;
    color: var(--white); line-height: 1;
  }
</style>
</head>
<body>

<section class="card card--front" aria-label="Card front">
  <svg class="card__shapes" width="620" height="354" viewBox="0 0 620 354">
    <path fill="var(--orange)" d="M0,0 H620 V46 Q470,22 350,40 L330,58 L310,44 L290,58 L270,40 Q150,22 0,46 Z"/>
    <rect x="30" y="318" width="560" height="7" rx="3.5" fill="var(--orange)"/>
  </svg>
  <p class="front-mark">KV7</p>
  <p class="front-shops">www.pohodanoviny.sk / www.relaxbrodeky.cz</p>
</section>

<section class="card card--back" aria-label="Card back">
  <svg class="card__shapes" width="620" height="354" viewBox="0 0 620 354">
    <rect x="32" y="42" width="7" height="282" rx="3.5" fill="var(--orange)"/>
    <path fill="var(--white)" d="M327,0 C352,40 377,110 370,160 L344,183 L370,190 C374,260 347,320 330,354 H620 V0 Z"/>
    <path fill="var(--orange)" d="M336,0 C361,40 386,110 379,160 L353,183 L379,190 C383,260 356,320 339,354 H620 V0 Z"/>
  </svg>

  <div class="contact">
    <div class="contact__row">
      <svg class="contact__icon" width="16" height="14" viewBox="0 0 16 14"><path fill="var(--orange)" d="M1,4 Q8,-1 15,4 L13,6 L10,5 L10,3 L6,3 L6,5 L3,6 Z M4,7 H12 L14,13 H2 Z"/></svg>
      <div class="contact__lines">
        <span class="contact__label">Office</span><span class="contact__value">+421 (0) 947 618 204</span>
        <span class="contact__label">Private</span><span class="contact__value">+421 (0) 907 251 836</span>
      </div>
    </div>
    <div class="contact__row">
      <svg class="contact__icon" width="16" height="12" viewBox="0 0 16 12"><rect width="16" height="12" rx="1" fill="var(--orange)"/><path d="M1,1 L8,7 L15,1" fill="none" stroke="var(--card-dark)" stroke-width="1.4"/></svg>
      <div class="contact__lines">
        <span class="contact__label">E-mail</span><span class="contact__value">info@kv7example.sk</span>
      </div>
    </div>
    <div class="contact__row">
      <svg class="contact__icon" width="16" height="14" viewBox="0 0 16 14"><rect x="1" y="1" width="14" height="9" fill="none" stroke="var(--orange)" stroke-width="2"/><rect x="5" y="11" width="6" height="2" fill="var(--orange)"/></svg>
      <div class="contact__lines">
        <span class="contact__label">Web</span><span class="contact__value">www.kv7example.sk</span>
      </div>
    </div>
    <div class="contact__row">
      <svg class="contact__icon" width="14" height="18" viewBox="0 0 14 18" style="margin-top:22px"><path fill="var(--orange)" d="M7,0 C3,0 0,3 0,7 C0,11 7,18 7,18 C7,18 14,11 14,7 C14,3 11,0 7,0 Z"/><circle cx="7" cy="7" r="2.6" fill="var(--card-dark)"/></svg>
      <p class="contact__address">Brezovanská 742/3,<br>931 05 Nová Breza,<br>Slovak republic (Slovakia)</p>
    </div>
  </div>

  <div class="owner">
    <p><span class="owner__name">Peter Hulka</span><span class="owner__title">, MSc. / CEO</span></p>
    <p class="owner__company">kV7 s.r.o.</p>
  </div>
  <p class="back-mark">KV7</p>
</section>

</body>
</html>
```